Redesign Of Flower Delivery Subscription Service Website

I need a revamped website of www.petal-rush.com

Please revamp current design using same content....

Target Market(s)

people who buy flowers. Brides, wedding planners, wedding photographer, married man, boyfriend, etc.

Industry/Entity Type

Florist

Number of Pages Required

5+ page

Colors

Designer to choose colors to be used in the design.

Requirements
Must have
• I need a revamped website of www.petal-rush.com
• Please revamp current design using same content....
Nice to have
Should not have

```html
<!DOCTYPE html>
<html lang="en">
<head>
<meta charset="utf-8">
<title>Petal Rush – Monthly Flowers Delivery</title>
<link href="https://fonts.googleapis.com/css2?family=Kaushan+Script&family=Montserrat:wght@400;500;600;700&display=swap" rel="stylesheet">
<style>
:root{
  --green:#8cc63f;
  --green-dark:#76ad2f;
  --orange:#f7941d;
  --ink:#555b60;
  --ink-soft:#7a7f84;
  --white:#ffffff;
}
*{box-sizing:border-box;margin:0;padding:0}
html,body{width:1200px;height:4245px;overflow:hidden}
body{position:relative;background:var(--white);font-family:"Montserrat",sans-serif;color:var(--ink)}
.script{font-family:"Kaushan Script",cursive;color:var(--green);font-weight:400}

/* header + hero */
.hero{position:absolute;left:0;top:0;width:1200px;height:675px;background:linear-gradient(180deg,#f1f1f2,#e4e4e6)}
.brand{position:absolute;left:122px;top:30px}
.brand-name{font-size:44px;font-weight:700;color:var(--green);letter-spacing:1px;line-height:1}
.brand-tag{font-size:12px;color:var(--ink-soft);margin-top:6px}
.utility{position:absolute;right:118px;top:26px;display:flex;align-items:center;gap:18px;font-size:13px;color:var(--ink-soft)}
.utility .util-link{display:flex;align-items:center;gap:6px}
.btn-buy{background:var(--orange);color:var(--white);font-weight:700;font-size:12px;padding:8px 18px;border-radius:20px}
.social{display:flex;gap:10px}
.social span{width:28px;height:28px;border-radius:50%;background:var(--green);display:block}
.main-nav{position:absolute;right:118px;top:80px;display:flex;gap:20px;font-size:13px;color:var(--ink-soft)}
.main-nav .active{color:var(--green);border-bottom:2px solid var(--green);padding-bottom:3px}
.hero-photo{position:absolute;left:680px;top:130px;width:420px;height:420px;border-radius:40% 50% 45% 50%;background:radial-gradient(circle at 45% 35%,#f2a6c2,#e27fa6 45%,rgba(120,170,90,.35) 75%,rgba(228,228,230,0) 100%)}
.hero-title{position:absolute;left:122px;top:235px;font-size:68px;line-height:1}
.hero-sub{position:absolute;left:122px;top:335px;font-size:21px;line-height:32px;color:var(--ink)}
.hero-sub strong{color:var(--orange)}
.hero-badges{position:absolute;left:122px;top:443px;display:flex;gap:30px}
.badge{width:150px;height:46px;border-radius:23px;background:var(--green);color:var(--white);font-size:13px;font-weight:700;display:flex;align-items:center;justify-content:center}

/* features */
.features{position:absolute;left:0;top:675px;width:1200px;height:725px;display:flex;justify-content:center;gap:52px;padding-top:68px}
.feature{width:280px;text-align:center}
.feature-photo{width:272px;height:358px;margin:0 auto}
.feature h3{font-size:24px;margin:30px 0 16px;white-space:nowrap}
.feature p{font-size:14px;line-height:23px;color:var(--ink)}

/* upgrade band */
.upgrade{position:absolute;left:0;top:1400px;width:1200px;height:880px;background:radial-gradient(ellipse at 50% 55%,#dcc7a6 0 30%,#b9a88f 45%,#7f8c6f 75%,#5f6a52 100%)}
.upgrade-title{position:absolute;left:0;width:1200px;top:385px;text-align:center;font-size:50px}
.signup{position:absolute;left:312px;top:472px;width:516px;height:48px;background:var(--white);border-radius:24px;display:flex;align-items:center;justify-content:space-between;padding-left:28px}
.signup span{font-size:14px;color:var(--ink-soft)}
.signup b{height:48px;width:150px;border-radius:24px;background:var(--green);color:var(--white);font-size:13px;display:flex;align-items:center;justify-content:center}

/* article */
.article{position:absolute;left:205px;top:2355px;width:795px}
.article h1{font-size:64px;line-height:1.1}
.article .lead{font-size:18px;margin:16px 0 24px}
.article p{font-size:14px;line-height:22px;color:var(--ink-soft)}
.article h2{font-size:32px;line-height:42px;margin:30px 0 20px}

/* footer */
.footer{position:absolute;left:0;top:3845px;width:1200px;height:355px;background:var(--green)}
.footer-badge{position:absolute;left:450px;top:-10px;width:300px;height:150px;background:var(--white);border-radius:0 0 150px 150px;text-align:center;padding-top:36px}
.footer-badge .brand-name{font-size:38px}
.footer-cols{position:absolute;left:0;top:160px;width:1200px;display:flex;justify-content:center;gap:50px;text-align:center;color:var(--white)}
.footer-col{width:270px}
.footer-col h4{font-family:"Kaushan Script",cursive;font-weight:400;font-size:22px;margin-bottom:14px}
.footer-col li{list-style:none;font-size:14px;line-height:24px}
.copyright{position:absolute;left:0;top:4200px;width:1200px;height:45px;background:var(--green-dark);color:var(--white);font-size:13px;display:flex;align-items:center;justify-content:center;gap:30px}
</style>
</head>
<body>

<section class="hero">
  <div class="hero-photo" role="img" aria-label="Photo of a single pink rose lying on a light grey surface"></div>
  <div class="brand">
    <div class="brand-name">Petal Rush</div>
    <div class="brand-tag">San Diego Flower Company</div>
  </div>
  <div class="utility">
    <span class="util-link"><svg width="12" height="12" viewBox="0 0 12 12"><circle cx="6" cy="6" r="5.5" fill="#7a7f84"/></svg>Help</span>
    <span class="util-link"><svg width="12" height="12" viewBox="0 0 12 12"><circle cx="6" cy="4" r="2.5" fill="#7a7f84"/><path d="M1 12a5 4 0 0 1 10 0z" fill="#7a7f84"/></svg>My Account</span>
    <span class="btn-buy">BUY NOW</span>
    <div class="social"><span></span><span></span><span></span><span></span></div>
  </div>
  <nav class="main-nav">
    <span class="active">Home</span><span>How it Works</span><span>Delivery Areas</span><span>Franchise</span><span>Blog</span><span>Free Flowers Monthly</span><span>Corporate Arrangements</span>
  </nav>
  <div class="hero-title script">Always Fresh</div>
  <div class="hero-sub">Beautiful Flower Arrangements Delivered Monthly<br>Now only <strong>$69.95/MTH</strong> ($100 value)</div>
  <div class="hero-badges"><span class="badge">FREE VASE</span><span class="badge">FREE DELIVERY</span><span class="badge">FREE UPGRADE</span></div>
</section>

<section class="features">
  <div class="feature">
    <div class="feature-photo" role="img" aria-label="Purple and white bouquet in a glass vase" style="background:linear-gradient(160deg,#7a4f8e,#b48cc0 50%,#d8d2d8)"></div>
    <h3 class="script">Set it and forget it</h3>
    <p>Petal Rush is a "SET IT and FORGET IT" subscription based flower delivery service. For an amazing price Petal Rush will hand deliver a gorgeous arrangement directly to anyone you want every month without you having to worry about it.</p>
  </div>
  <div class="feature">
    <div class="feature-photo" role="img" aria-label="Cream and pink rose bouquet in a glass vase" style="background:linear-gradient(160deg,#e9dfb8,#e8c9c4 50%,#f1ede6)"></div>
    <h3 class="script">But never forget again</h3>
    <p>When setting up your account, you can choose exact delivery dates for the months that have special days such as your Anniversary, Birthday, Valentines Day and Mothers Day. You might forget but we won't, we have got ya covered!</p>
  </div>
  <div class="feature">
    <div class="feature-photo" role="img" aria-label="Coral roses arranged in a red vase" style="background:linear-gradient(160deg,#f4f4f4,#f19b86 45%,#e6e6e6)"></div>
    <h3 class="script">Making someone's day better</h3>
    <p>Be the hero in that special someone's life each and every month. It feels good to make a difference in your loved one's day.</p>
  </div>
</section>

<section class="upgrade" role="img" aria-label="Florist workbench with tulips, twine, scissors and kraft paper">
  <div class="upgrade-title script">Receive A Free Upgrade</div>
  <div class="signup"><span>Enter Your Email</span><b>SUBSCRIBE NOW</b></div>
</section>

<article class="article">
  <h1 class="script">Monthly Subscription</h1>
  <p class="lead">Based Flower Delivery Service in San Diego - CA by Our Florist Shop</p>
  <p>Every moment of life could be cherished perfectly.....If you choose wisely. To make your day more treasured, remember that flowers are the smartest choice when delivered through our monthly Petal Rush subscription based delivery service. Our online subscription-based flower delivery service can help you pamper, cherish and make an everlasting impression on the minds of your loved ones with a doorstep delivery of exquisitely hand-designed floral arrangements. Our online subscription service features both standard and personalized services to help you choose from an assortment of classic and contemporary floral arrangements. It is your chance to setup a weekly, monthly, or quarterly subscription, so we can deliver the most exotic collections of hand-decorated flowers that you and your loved ones will cherish.</p>
  <h2 class="script">Exotic Flowers Garnished With Special Hues<br>To Compliment Your Loved Ones</h2>
  <p>Let's not forget a single day in which you can make your loved ones feel special. Whether it's your anniversary or a birthday in your family, you must always go an extra mile to show "how much I care about you." Nothing can compare to your show of love, or compliment the joy of your loved ones, more than a perfectly blossomed bouquet of flowers. So if you are having difficulty in finding the perfect flower bouquet to share your overflowing love with that special person, don't worry.....Petal Rush has got it all covered for you! We believe that our hand-picked and hand-designed flowers, created with a combination of lavish designs and feminine hues, will definitely grab the attention of your loved ones. At Petal Rush, we deliver both birthday flowers and sympathy flowers garnished with special hues of love and support. Our bouquets share your side of affection and sorrow with your loved ones on any memorable day of their lives.</p>
  <h2 class="script">Standard And Personalized Flower<br>Arrangements For Special Occasions</h2>
  <p>Petal Rush offers on time subscription based service that is risk free, trouble free and affordable at the same time. We offer the most trusted and delightful flower delivery service in San Diego, and are designed to deliver your desired floral arrangements within your requested days and times. Our local florists will happily take your orders online for your shopping convenience. You can count on us to deliver fresh flower baskets and bouquets for birthdays, weddings, mother's day, anniversaries and other special events within your locality, and even across the country. In case you're looking for something personalized, then our skilled florists can create custom arrangements for any special occasion. Get Yourself Subscribed And Claim Discounts On Big Orders!</p>
  <h2 class="script">Get Yourself Subscribed And Claim<br>Discounts On Big Orders!</h2>
  <p>Get love and adulation by gifting flowers to your loved ones on those special occasions. Whether it's formal, personal or your love for your family, just follow the subscription criteria and get your hands on the most valuable service for all kinds of events, occasions and parties. Set up your account and select the right delivery dates for the special months and leave the rest to us. We will deliver your flowers on the exact special dates to make your loved one's day wonderful. It is your chance to experience the simple, risk free and trouble free delivery of flowers right to the doorstep of your cherished loved.</p>
</article>

<footer class="footer">
  <div class="footer-badge">
    <div class="brand-name">Petal Rush</div>
    <div class="brand-tag">San Diego Flower Company</div>
  </div>
  <div class="footer-cols">
    <div class="footer-col"><h4>More Services</h4><ul><li>Corporate Arrangements</li><li>Hotel Arrangements</li><li>Events</li><li>Weddings</li></ul></div>
    <div class="footer-col"><h4>Other Links</h4><ul><li>Terms and Services</li><li>Privacy Policy</li><li>FAQ's</li></ul></div>
    <div class="footer-col"><h4>Contact</h4><ul><li>Phone: (619) 555-0142</li><li>support@petal-rush.com</li><li>1840 Harbor View Lane El Cajon,</li><li>San Diego CA 92020</li></ul></div>
  </div>
</footer>
<div class="copyright"><span>Petal Rush - Monthly Flowers Delivery</span><span>Copyright 2016. All Rights Reserved.</span></div>

</body>
</html>
```